Bright Path Attorneys Billboard Design for Personal Injury Law Firm

Need a billboard design that we can use for different versions. 1400px X 400px jpeg or png
I have attached the logo and the attorney for the billboard. Attorney Marla Benning
Here is a link to our current website brightpathlegalgroup.example

HEADLINE: HIT BY A TRUCK?
SUBHEAD: NO FEE. BIG FIGHT.
877-GRANTLY

HEADLINE: ACCIDENT?
SUBHEAD: NO FEE, UNLESS WE WIN!
877-GRANTLY

HEADLINE: BIG TRUCK. BIG CASE.
SUBHEAD: YOU PAY $0 UPFRONT
877-GRANTLY

Target Market(s)

People in Car Accident

Industry/Entity Type

Personal Injury Attorneys

```html
<!DOCTYPE html>
<html lang="en">
<head>
<meta charset="utf-8">
<title>Bright Path Attorneys – Accident Billboard</title>
<link rel="stylesheet" href="https://fonts.googleapis.com/css2?family=Anton&family=Montserrat:wght@700;800&display=swap">
<style>
  :root {
    --page: #ffffff;
    --navy-deep: #05285a;
    --blue-mid: #063e88;
    --blue-bright: #0a66c8;
    --gold: #fdbe00;
    --white: #ffffff;
    --photo-dark: #1c2a4a;
    --photo-light: #c9a27c;
  }
  * { margin: 0; padding: 0; box-sizing: border-box; }
  html, body {
    width: 1074px;
    height: 1200px;
    overflow: hidden;
    background: var(--page);
  }
  .billboard {
    position: absolute;
    left: 84px;
    top: 471px;
    width: 906px;
    height: 259px;
    overflow: hidden;
    background: linear-gradient(90deg, var(--navy-deep) 0%, var(--blue-mid) 45%, var(--blue-bright) 100%);
    box-shadow: 0 6px 22px rgba(0, 0, 0, 0.45);
  }
  .message {
    position: absolute;
    left: 0;
    top: 0;
    width: 700px;
    height: 100%;
    text-align: center;
    z-index: 2;
  }
  .headline {
    position: absolute;
    left: 0;
    right: 0;
    top: 12px;
    font-family: "Anton", "Oswald", sans-serif;
    font-weight: 400;
    font-size: 127px;
    line-height: 1;
    color: var(--gold);
    letter-spacing: 4px;
    transform: scaleX(1.06);
  }
  .subhead {
    position: absolute;
    left: 0;
    right: 0;
    top: 140px;
    font-family: "Montserrat", sans-serif;
    font-weight: 800;
    font-size: 44px;
    line-height: 1;
    color: var(--white);
    letter-spacing: 0.5px;
  }
  .phone {
    position: absolute;
    left: -6px;
    right: 0;
    top: 198px;
    font-family: "Montserrat", sans-serif;
    font-weight: 800;
    font-size: 50px;
    line-height: 1;
    color: var(--gold);
  }
  .firm-name {
    position: absolute;
    left: 566px;
    top: 229px;
    z-index: 3;
    display: flex;
    align-items: center;
    gap: 5px;
    font-family: "Montserrat", sans-serif;
    font-weight: 700;
    font-size: 9px;
    line-height: 1.1;
    color: var(--white);
    white-space: nowrap;
  }
  .firm-dot {
    width: 9px;
    height: 9px;
    border-radius: 50%;
    background: var(--white);
    flex: none;
  }
  .sun-circle {
    position: absolute;
    left: 678px;
    top: 8px;
    width: 208px;
    height: 208px;
    border-radius: 50%;
    background: var(--gold);
    z-index: 1;
  }
  .attorney-photo {
    position: absolute;
    left: 678px;
    top: 6px;
    width: 190px;
    height: 253px;
    border-radius: 80px 80px 0 0;
    background: linear-gradient(180deg, var(--photo-light) 0%, #8a6a52 32%, var(--photo-dark) 62%, #16213b 100%);
    z-index: 1;
  }
</style>
</head>
<body>
  <section class="billboard">
    <div class="sun-circle"></div>
    <div class="attorney-photo" role="img" aria-label="Portrait of attorney Marla Benning in a navy blazer, arms crossed, smiling"></div>
    <div class="message">
      <h1 class="headline">ACCIDENT?</h1>
      <p class="subhead">NO FEE, UNLESS WE WIN!</p>
      <p class="phone">877-GRANTLY</p>
    </div>
    <div class="firm-name"><span class="firm-dot"></span><span>BRIGHT PATH<br>ATTORNEYS</span></div>
  </section>
</body>
</html>
```